Summer orchestra weekly camp poster BVSE youth orchestra

We are youth orchestra in Texas holds a summer program called: Bright Bows Holiday Workshop (It's for students ages 8-18 who play already play violin/viola/cello/bass in the North Dallas, Texas Area.

We have 2 posters already from Artpitchly designers that we have already been using and now are looking for some new designs. (you can see our other two previously purchased designs on the art pitchly website)

The main difference in our camp is that we meet weekly on Saturday for 2 months June and July (not a week or 2 long camp like most music camps). This makes us a better choice locally because you are playing every week for 2 months out if the summer and less likely to lose skills over the summer vacation months.

Poster size: 11" by 17" but needs to be convertible to 8.5 to 11 size as well AND most importantly be in editable format via either Word or Publisher so we can use it every summer and be able to change dates, cost or location as needed.

All the details are below, but on the poster we would need the website listed: www.brenwickvalleystrings.example and tell them to go to that website to apply online beginning April 1st

That's how we get business, they go to our website and apply and pay with coinvane. It also needs to say really big BVSE BRIGHT BOWS HOLIDAY WORKSHOP

April 1st is when we being accepting online applications (every year, so don't put a year) Also put: Camp is held on Saturdays in June and July with final concert, last Sunday in July

Also on the poster we need: Our goal is to keep young musicians playing over the summer –so don’t put your instrument away for the summer! Keep in shape by joining us for the Brenwick Valley String Ensemble’s summer program – Bright Bows Holiday Workshop! Tuition is $225, which covers June/July Saturday rehearsals and the performance fee for the GUSD FAH concert, last Sunday in July.

I know we can't get all the info below on it, but I put it on so you could better understand what we are doing.

We have a logo already, that we have the rights to - I need something that kids/teens will think is cool looking and music related....we are string instruments only (violin, viola, cello, bass) we also want it to look classy looking, not cheap
I included 2 copies of the logo in different color set

here's all the details from our website:
Bright Bows Holiday Workshop (June and July) - Tuition: $225
Somewhere it should stress that we are not like other camps because we are weekly for two months. (There's a better way to state that but I'm not sure what that is)

Rehearsals on Saturdays June &July with final concert on last Sunday in July @ GHS FAH

Our goal is to keep young musicians playing over the summer –so don’t put your instrument away for the summer! Keep in shape by joining us for the Brenwick Valley String Ensemble’s new summer program – Bright Bows Holiday Workshop!

Tuition is $225, which covers June/July Saturday rehearsals and the performance fee for the GUSD FAH concert.

No audition is necessary. Enrollment is limited to the first 50 students in each age category, depending on instrumentation needs, so don’t delay – enrollment online begins April 1st. Siblings will receive a $50 discount, after the first child's regular priced tuition.

Bright Bows I: Students entering grades 6 and below (3:00 – 4:20 P.M. )
Bright Bows II: Students grades entering 7 and 8 (4:30 – 6:00 P.M.)
Bright Bows III: Students entering grades 9-12 (6:15 – 7:45 P.M.)

Summer camp attendance policy is more lenient due to summer vacations. Please notify BVSE of summer absences as soon as your vacation/camp dates are known.

Here is a link to the previous contest we held on ArtPitchly last year.

http://jobs.artpitchly.example/job.aspx?id=584316

http://poster.artpitchly.example/contest.aspx?id=584316

Also Rehearsals are held at Marlow Fiddleworks in Allen, TX

I am working today at a music festival and cannot get on the computer or artpitchly website until after 6 or 7 p.m. tonight.  So if you are not getting feedback during the day today, that is why.  I will give feedback to everyone when I get home later tonight.  Thank you all for your work!

Reason: Hi everyone, I judged a music contest all day today and really need some time to look over all the entries. I appreciate everyone's hard work and will make a decision within the next 2 days. I want to be able to provide feedback to everyone and give everyone enough time to submit their best work, so I am extending the deadline by 2 days. I will have to make a decision at the end very quickly as we need to do a huge mail out as soon as the contest is over. Thank you everyone, we really do appreciate everyone's efforts in making our new poster for Bright Holiday Bows Workshop!

Target Market(s)

Parents of string players age 8-18 in North Texas along with students themselves.

Industry/Entity Type

Business

Requirements
Must have
• something showing we are different than the ordinary summer music camp
our QR code which I will email to you if your poster is the winner

```html
<!DOCTYPE html>
<html lang="en">
<head>
<meta charset="utf-8">
<title>BVSE Bright Bows Holiday Workshop</title>
<link href="https://fonts.googleapis.com/css2?family=Tinos:ital,wght@1,700&family=Carlito:ital,wght@0,400;0,700;1,400;1,700&family=Open+Sans:ital,wght@0,400;0,600;0,700;1,400&family=Fondamento&display=swap" rel="stylesheet">
<style>
  :root {
    --sky: #bfe9e6;
    --blush: #f3b6a6;
    --coral: #ee7d66;
    --ember: #d9533f;
    --ink: #111111;
    --paper: #ffffff;
    --band: rgba(248, 244, 242, 0.88);
    --box: rgba(170, 160, 160, 0.55);
    --rule: #555555;
    --pay: #1b3f8a;
  }
  * { margin: 0; padding: 0; box-sizing: border-box; }
  html, body { width: 776px; height: 1200px; overflow: hidden; background: var(--paper); }
  .poster {
    position: relative; width: 776px; height: 1200px; overflow: hidden;
    font-family: "Carlito", "Calibri", sans-serif; color: var(--ink);
  }
  .photo {
    position: absolute; inset: 0;
    background:
      radial-gradient(ellipse 260px 180px at 220px 1010px, rgba(255,255,255,0.45), transparent 70%),
      radial-gradient(ellipse 420px 300px at 600px 380px, rgba(200,70,50,0.35), transparent 70%),
      linear-gradient(180deg, var(--sky) 0%, #e9d3c8 8%, var(--blush) 16%, var(--coral) 35%, var(--ember) 60%, var(--coral) 80%, #f0a490 100%);
  }
  .title {
    position: absolute; left: 0; width: 776px; text-align: center; white-space: nowrap;
    font-family: "Tinos", "Times New Roman", serif; font-style: italic; font-weight: 700;
    color: var(--paper); text-shadow: 3px 3px 3px rgba(0,0,0,0.45);
    line-height: 1; font-size: 66px;
  }
  .title-top { top: 4px; }
  .title-bottom { top: 98px; }
  .pitch {
    position: absolute; left: 22px; top: 262px; width: 225px;
    transform: rotate(-21deg); transform-origin: left top;
    font-family: "Open Sans", sans-serif;
    color: #2a1a18; line-height: 1.08;
  }
  .pitch-goal { font-size: 15px; }
  .pitch-join { font-size: 18px; margin-top: 6px; }
  .pitch-name { font-size: 22px; font-weight: 700; }
  .dates {
    position: absolute; left: 450px; top: 218px; width: 262px; height: 228px;
    background: var(--box); border-radius: 22px;
    padding: 12px 10px 0 12px;
    font-family: "Open Sans", sans-serif; font-weight: 600;
    font-size: 19px; line-height: 34px; letter-spacing: 1.2px; text-align: justify;
  }
  .apply {
    position: absolute; left: 0; top: 515px; width: 776px; height: 225px;
    background: var(--band);
    border-top: 3px solid var(--rule); border-bottom: 2px solid var(--rule);
    text-align: center; font-family: "Open Sans", sans-serif;
  }
  .apply-heading { position: absolute; top: 14px; width: 100%; font-size: 43px; font-weight: 400; letter-spacing: 0.5px; }
  .apply-note { position: absolute; top: 82px; width: 100%; font-style: italic; font-size: 19px; color: #222; }
  .apply-open { position: absolute; top: 122px; width: 100%; font-size: 24px; }
  .apply-url {
    position: absolute; top: 170px; width: 100%; font-size: 30px; font-weight: 700;
    text-shadow: 2px 2px 2px rgba(0,0,0,0.35);
  }
  .fee {
    position: absolute; right: 30px; top: 748px;
    font-family: "Open Sans", sans-serif; font-weight: 700; font-size: 44px;
  }
  .includes { position: absolute; left: 10px; top: 798px; width: 192px; font-size: 16px; font-weight: 700; line-height: 26px; }
  .includes-head { padding-left: 29px; }
  .includes ul { list-style: none; }
  .includes li::before { content: "\2022"; padding-left: 2px; padding-right: 4px; }
  .includes .venue { font-style: italic; padding-left: 12px; display: block; }
  .different {
    position: absolute; left: 468px; top: 847px; width: 288px; height: 295px;
    background: var(--box); padding: 16px 8px 0;
    text-align: center; font-style: italic; font-size: 17.5px; line-height: 28px;
  }
  .different-head { font-weight: 700; margin-bottom: 2px; }
  .different p::before { content: "\266B\00a0"; font-style: normal; font-size: 13px; }
  .different p.different-head::before { content: none; }
  .limit { position: absolute; left: 146px; top: 1047px; font-size: 14px; font-style: italic; font-weight: 700; }
  .perk { position: absolute; font-family: "Fondamento", serif; font-size: 17px; letter-spacing: 0.4px; }
  .perk-audition { left: 96px; top: 1078px; }
  .perk-sibling { left: 112px; top: 1118px; }
  .payment {
    position: absolute; left: 24px; top: 1124px; display: flex; align-items: center; gap: 4px;
    font-size: 13px; font-weight: 700; color: var(--pay);
  }
  .payment-mark { width: 11px; height: 11px; background: var(--pay); }
  .footer {
    position: absolute; left: 0; top: 1168px; width: 776px;
    text-align: center; font-size: 14px; font-style: italic; color: #222;
  }
  .footer b { font-style: normal; color: var(--ink); }
</style>
</head>
<body>
<main class="poster">
  <div class="photo" role="img" aria-label="Close-up photograph of a red violin body, f-hole and strings with faint music notes"></div>

  <h1 class="title title-top">BVSE BRIGHT BOWS</h1>
  <div class="title title-bottom">HOLIDAY WORKSHOP</div>

  <div class="pitch">
    <p class="pitch-goal">Our goal is to <b>keep young musicians playing</b> over the summer time; so don't put your instrument away <b>this summer!</b></p>
    <p class="pitch-join"><b>Keep in shape</b> by joining us for the <b>Brenwick Valley String Ensemble's</b> New Summer Program:</p>
    <p class="pitch-name">Bright Bows Holiday Workshop</p>
  </div>

  <div class="dates">Bright Bows Holiday Workshop taking place Saturdays during June &amp; July with a Final Concert held on the last Sunday in July.</div>

  <section class="apply">
    <h2 class="apply-heading">GO ONLINE TO APPLY</h2>
    <p class="apply-note">Visit our site to apply and submit your application to secure your space<sup>*</sup></p>
    <p class="apply-open">Online Applications Open 1 April</p>
    <p class="apply-url">www.brenwickvalleystrings.example</p>
  </section>

  <div class="fee">TUITION FEE: $225</div>

  <div class="includes">
    <p class="includes-head">Fee Includes :-</p>
    <ul>
      <li>All rehearsals on Saturdays&nbsp; for June &amp; July</li>
      <li>Performance Fee <span class="venue">(GUSD FAH Concert - Last Sunday of July)</span></li>
    </ul>
  </div>

  <div class="different">
    <p class="different-head">We Are Different To The Rest</p>
    <p>Runs on Saturdays for a period of <b>2 months,</b> making it a better choice locally;</p>
    <p>Gives you the opportunity to <b>play every week</b> for a <b>full 2 months</b> over summer vacation time; making you less likely to lose skills.</p>
  </div>

  <p class="limit">*Limited to 50 Entrants Per Age&nbsp; category</p>
  <p class="perk perk-audition">No&nbsp; Auditions&nbsp; Necessary</p>
  <p class="perk perk-sibling">Siblings&nbsp; get&nbsp; $50&nbsp; off</p>

  <div class="payment"><span class="payment-mark"></span>Coinvane</div>

  <p class="footer">For more information, rehearsal times and online applications&nbsp; <b>www.brenwickvalleystrings.example</b></p>
</main>
</body>
</html>
```